Modern Label for cleaning products for the brand Voralux

We need a label design for our line of cleaning products. The label should feature our logo and an image to identify the product's intended use. I've added our logo and an image for use. This only concerns the design of the label on the front of the bottle.

Label dimensions:
Label 1 (500ml bottle with spray): width 58mm x height 115mm
Label 2: (1L bottle): width 73mm x height 140mm
The design must be consistent for both bottles which you find in the pictures.

The bottles to be labeled are white. See the attachment for a photo of the bottles.

The photo must also appear on the label to identify the product's intended use.

Product information:
Brand: Voralux
Product: Sanitary Cleaner

This text must be placed on the label:
"Cleans, descales & freshens. followed with this text: "Ideal for quick and powerful cleaning. A ready-to-use product for everyday use."

- Mention the seperate USP's: Sanitary, Bathroom, Toilet, Wet areas

Appearance: This is a consumer product, but it must have a professional appearance. We would like to see a design that use the color blue from our logo.

Target Market(s)

Consumers who take care of their homes and want to maintain it the correct (professional) way

Font styles to use
Sans Serif

Colors
0054AA
0677BA
7BADD7
CADEEF
E8F1F8

Requirements
Must have
• USP's + use of image and logo + blend in 1 design
Nice to have
• Keep the color of the logo in the design
Should not have
• Comic sans

```html
<!DOCTYPE html>
<html lang="en">
<head>
<meta charset="utf-8">
<title>Voralux Sanitary Cleaner – Labels</title>
<link rel="stylesheet" href="https://fonts.googleapis.com/css2?family=Poppins:wght@600;800&family=Roboto:wght@300;400&family=Roboto+Condensed:wght@400;700&display=swap">
<style>
  :root {
    --brand-blue: #0054AA;
    --mid-blue: #0677BA;
    --soft-blue: #7BADD7;
    --pale-blue: #CADEEF;
    --mist-blue: #E8F1F8;
    --brand-grey: #6d6e71;
    --accent-silver: #b8c4cf;
    --white: #ffffff;
    --edge: #d9dde2;
  }
  html, body {
    margin: 0;
    padding: 0;
    width: 1200px;
    height: 649px;
    overflow: hidden;
    background: var(--white);
  }
  .canvas {
    position: relative;
    width: 1200px;
    height: 649px;
  }
  .art-defs {
    position: absolute;
    width: 0;
    height: 0;
  }
  .label {
    position: absolute;
    height: auto;
  }
  .label--500-flat   { left: 82px;  top: 170px; width: 202px; }
  .label--1l-flat    { left: 321px; top: 89px;  width: 254px; }
  .label--500-bottle { left: 649px; top: 272px; width: 151px; }
  .label--1l-bottle  { left: 924px; top: 215px; width: 183px; }

  .brand-name   { font: 600 38px "Poppins", sans-serif; fill: var(--brand-grey); letter-spacing: -0.5px; }
  .product-name { font: 800 36px "Poppins", sans-serif; fill: var(--white); letter-spacing: -0.5px; }
  .claim        { font: 300 16.5px "Roboto", sans-serif; fill: var(--white); }
  .ideal-line   { font: 400 10.6px "Roboto Condensed", sans-serif; fill: var(--white); }
  .ideal-line .highlight { font-weight: 700; fill: var(--accent-silver); }
  .usp-label    { font: 400 9.6px "Roboto", sans-serif; fill: var(--soft-blue); }
  .usage-note   { font: 400 11.4px "Roboto", sans-serif; fill: var(--white); }
  .volume       { font: 400 14px "Roboto", sans-serif; fill: var(--white); }
  .usp-icon     { fill: none; stroke: var(--soft-blue); stroke-width: 1.6; stroke-linecap: round; stroke-linejoin: round; }
  .usp-divider  { stroke: var(--soft-blue); stroke-width: 0.8; opacity: 0.7; }
  .label-edge   { fill: none; stroke: var(--edge); stroke-width: 1.2; }
</style>
</head>
<body>
<main class="canvas">

  <svg class="art-defs" aria-hidden="true" focusable="false">
    <defs>
      <linearGradient id="photo-tone" x1="0" y1="0" x2="1" y2="1">
        <stop offset="0" stop-color="#CADEEF"/>
        <stop offset="0.55" stop-color="#9fc2e2"/>
        <stop offset="1" stop-color="#7BADD7"/>
      </linearGradient>
      <linearGradient id="deep-tone" x1="0" y1="0" x2="0" y2="1">
        <stop offset="0" stop-color="#0054AA"/>
        <stop offset="1" stop-color="#0677BA"/>
      </linearGradient>
      <clipPath id="label-shape">
        <path d="M12,0 H258 Q270,0 270,12 V480 C225,508 60,516 0,470 V12 Q0,0 12,0 Z"/>
      </clipPath>
      <path id="sparkle" d="M0,-7 Q1,-1 7,0 Q1,1 0,7 Q-1,1 -7,0 Q-1,-1 0,-7 Z"/>

      <symbol id="label-art" viewBox="0 0 270 510">
        <g clip-path="url(#label-shape)">
          <rect class="label-base" width="270" height="510" fill="var(--white)"/>
          <g class="label-photo" role="img" aria-label="Photo of a bright blue tiled bathroom with a toilet, shower and plants">
            <rect x="0" y="80" width="270" height="260" fill="url(#photo-tone)"/>
          </g>
          <path class="label-header" d="M0,0 H270 V96 C205,168 90,182 0,152 Z" fill="var(--white)"/>
          <path class="label-footer" d="M0,318 C90,340 200,325 270,282 V510 H0 Z" fill="url(#deep-tone)"/>
        </g>

        <g class="brand-block">
          <circle cx="135" cy="60" r="30" fill="none" stroke="var(--brand-blue)" stroke-width="8"/>
          <text class="brand-name" x="135" y="133" text-anchor="middle">Voralux</text>
        </g>

        <g class="product-title">
          <text class="product-name" x="22" y="203">Sanitary</text>
          <text class="product-name" x="22" y="238">Cleaner</text>
          <text class="claim" x="24" y="264">Cleans, descales</text>
          <text class="claim" x="24" y="286">&amp; freshens</text>
        </g>

        <g class="sparkles" fill="var(--white)">
          <use href="#sparkle" transform="translate(202 173)"/>
          <use href="#sparkle" transform="translate(180 262)"/>
          <use href="#sparkle" transform="translate(233 291) scale(0.75)"/>
        </g>

        <text class="ideal-line" x="22" y="350">IDEAL FOR <tspan class="highlight">QUICK AND POWERFUL</tspan> CLEANING</text>

        <g class="usp-row">
          <line class="usp-divider" x1="70" y1="362" x2="70" y2="430"/>
          <line class="usp-divider" x1="131" y1="362" x2="131" y2="430"/>
          <line class="usp-divider" x1="193" y1="362" x2="193" y2="430"/>

          <g class="usp usp--sanitary">
            <g class="usp-icon" transform="translate(38 388)">
              <path d="M-13,-4 H13 Q12,9 0,9 Q-12,9 -13,-4 Z"/>
              <path d="M-3,9 V22 H3 V9"/>
              <path d="M-2,-4 V-14 Q-2,-19 3,-19 Q7,-19 7,-15"/>
            </g>
            <text class="usp-label" x="38" y="426" text-anchor="middle">Sanitary</text>
          </g>

          <g class="usp usp--bathroom">
            <g class="usp-icon" transform="translate(100 388)">
              <path d="M-18,4 H18 V8 Q18,18 8,18 H-8 Q-18,18 -18,8 Z"/>
              <path d="M-13,18 L-15,22 M13,18 L15,22"/>
              <path d="M-12,4 V-14 Q-12,-19 -7,-19 Q-3,-19 -3,-15"/>
              <path d="M-5,-11 V-9 M-2,-11 V-9"/>
            </g>
            <text class="usp-label" x="100" y="426" text-anchor="middle">Bathroom</text>
          </g>

          <g class="usp usp--toilet">
            <g class="usp-icon" transform="translate(162 388)">
              <rect x="-11" y="-20" width="22" height="10" rx="2"/>
              <ellipse cx="0" cy="-2" rx="11" ry="8"/>
              <path d="M-8,5 Q-6,14 -6,16 H6 Q6,14 8,5"/>
              <path d="M-6,21 H6 V16"/>
            </g>
            <text class="usp-label" x="162" y="426" text-anchor="middle">Toilet</text>
          </g>

          <g class="usp usp--wet-areas">
            <g class="usp-icon" transform="translate(219 388)">
              <path d="M0,-20 V-14"/>
              <path d="M0,-14 C12,-14 14,2 10,10 Q0,20 -10,10 C-14,2 -12,-14 0,-14 Z"/>
              <ellipse cx="0" cy="4" rx="6" ry="4"/>
            </g>
            <text class="usp-label" x="219" y="426" text-anchor="middle">Wet areas</text>
          </g>
        </g>

        <g class="usage-note-block">
          <text class="usage-note" x="24" y="462">A ready-to-use product</text>
          <text class="usage-note" x="24" y="476">for everyday use</text>
        </g>
      </symbol>
    </defs>
  </svg>

  <svg class="label label--500-flat" viewBox="0 0 270 510" role="group" aria-label="Voralux Sanitary Cleaner 500ml label">
    <use href="#label-art"/>
    <path class="label-edge" d="M12,0.6 H258 Q269.4,0.6 269.4,12 V480 C225,508 60,516 0.6,470 V12 Q0.6,0.6 12,0.6 Z"/>
    <text class="volume" x="246" y="488" text-anchor="end">500ml</text>
  </svg>

  <svg class="label label--1l-flat" viewBox="0 0 270 510" role="group" aria-label="Voralux Sanitary Cleaner 1L label">
    <use href="#label-art"/>
    <path class="label-edge" d="M12,0.6 H258 Q269.4,0.6 269.4,12 V480 C225,508 60,516 0.6,470 V12 Q0.6,0.6 12,0.6 Z"/>
    <text class="volume" x="246" y="482" text-anchor="end">1L</text>
  </svg>

  <svg class="label label--500-bottle" viewBox="0 0 270 510" role="group" aria-label="Voralux Sanitary Cleaner 500ml spray bottle label">
    <use href="#label-art"/>
    <text class="volume" x="246" y="488" text-anchor="end">500ml</text>
  </svg>

  <svg class="label label--1l-bottle" viewBox="0 0 270 510" role="group" aria-label="Voralux Sanitary Cleaner 1L bottle label">
    <use href="#label-art"/>
    <text class="volume" x="246" y="482" text-anchor="end">1L</text>
  </svg>

</main>
</body>
</html>
```